A billboard for Harlow Ridge Construction size 36.5’ x 14.5’

Hi guys. We are purchasing a billboard and are looking for a design (size 36.5’ x 14.5’). Our slogan is "Quality you deserve, service you can count on". The goal of this billboard is brand recognition primarily letting people know we do roofs. Attached are logos that can be used if needed. Not necessarily all of them need to be used.

Target Market(s)

Residents in the local areas needing or thinking about a roof replacement

Industry/Entity Type

Roofing

Requirements
Must have
• Logo and services (roof replacement, gutters, siding, and snow removal)
Nice to have
• take a look at our website for ideas www.harlowridgeconstruction.example

```html
<!DOCTYPE html>
<html lang="en">
<head>
<meta charset="utf-8">
<title>Harlow Ridge Construction Billboard</title>
<link href="https://fonts.googleapis.com/css2?family=Exo+2:wght@600;800;900&family=Poppins:ital,wght@0,600;0,700;1,500&display=swap" rel="stylesheet">
<style>
  :root {
    --stage: #2c313b;
    --panel: #252527;
    --red: #e3121b;
    --white: #ffffff;
    --ink: #1d1d1f;
    --badge-grey: #b9bcc0;
    --badge-dark: #2a2a2a;
    --badge-blue: #1f6a9c;
  }
  * { margin: 0; padding: 0; box-sizing: border-box; }
  html, body { width: 983px; height: 1200px; overflow: hidden; background: var(--stage); }
  .billboard { position: absolute; left: 30px; top: 416px; width: 923px; height: 367px; overflow: hidden; }
  .billboard-shapes { position: absolute; inset: 0; width: 100%; height: 100%; }
  .headline { position: absolute; left: 35px; font-family: "Exo 2", sans-serif; font-weight: 900; line-height: 1; white-space: nowrap; }
  .headline-quality { top: 52px; font-size: 45px; letter-spacing: 0.3px; color: var(--white); }
  .headline-service { top: 106px; font-size: 39px; letter-spacing: 0; color: var(--red); }
  .headline-rule { position: absolute; left: 35px; top: 160px; width: 221px; height: 3px; background: var(--red); }
  .services { position: absolute; left: 35px; list-style: none; display: flex; gap: 10px; font-family: "Poppins", sans-serif; font-style: italic; font-weight: 500; font-size: 17px; color: var(--white); white-space: nowrap; }
  .services-row-one { top: 178px; }
  .services-row-two { top: 206px; }
  .services li { display: flex; align-items: center; gap: 3px; }
  .services svg { width: 15px; height: 15px; flex: none; }
  .contact { position: absolute; left: 42px; top: 296px; font-family: "Exo 2", sans-serif; color: var(--ink); }
  .contact-phone { font-weight: 800; font-size: 32px; line-height: 1; letter-spacing: 0.5px; }
  .contact-web { font-family: "Poppins", sans-serif; font-weight: 600; font-size: 12.5px; margin-top: 3px; }
  .divider { position: absolute; top: 312px; width: 2px; height: 42px; background: var(--ink); }
  .divider-left { left: 292px; }
  .divider-right { left: 623px; }
  .brand { position: absolute; left: 326px; top: 304px; display: flex; align-items: center; gap: 12px; }
  .brand-square { width: 14px; height: 14px; background: var(--red); }
  .brand-name { font-family: "Exo 2", sans-serif; font-weight: 600; font-size: 24px; line-height: 1.05; color: var(--ink); }
  .badge { position: absolute; }
  .badge-one { left: 648px; top: 312px; width: 44px; height: 40px; background: var(--badge-grey); border-radius: 4px; }
  .badge-two { left: 716px; top: 312px; width: 68px; height: 40px; background: var(--badge-dark); border-radius: 4px; }
  .badge-three { left: 808px; top: 310px; width: 96px; height: 36px; background: var(--badge-blue); border-radius: 3px; }
</style>
</head>
<body>
<main class="billboard">
  <svg class="billboard-shapes" viewBox="0 0 923 367">
    <defs>
      <linearGradient id="photoTone" x1="0" y1="0" x2="0" y2="1">
        <stop offset="0" stop-color="#3f86cf"/>
        <stop offset="0.35" stop-color="#8fb6d8"/>
        <stop offset="0.55" stop-color="#8d735d"/>
        <stop offset="0.85" stop-color="#6f6150"/>
        <stop offset="1" stop-color="#5d7a45"/>
      </linearGradient>
    </defs>
    <rect width="923" height="367" fill="var(--panel)"/>
    <g role="img" aria-label="Photo of a brick family home with a new shingle roof under blue sky">
      <polygon points="641,0 923,0 923,292 600,263" fill="url(#photoTone)"/>
    </g>
    <polygon points="632,0 641,0 600,263 590,262" fill="var(--red)"/>
    <polygon points="0,268 461,243 923,288 923,300 461,253 0,279" fill="var(--red)"/>
    <polygon points="0,279 461,253 923,300 923,367 0,367" fill="var(--white)"/>
  </svg>

  <h1 class="headline headline-quality">QUALITY YOU DESERVE</h1>
  <h2 class="headline headline-service">SERVICE YOU CAN COUNT ON</h2>
  <div class="headline-rule"></div>

  <ul class="services services-row-one">
    <li><svg viewBox="0 0 16 16"><rect x="1" y="3" width="12" height="12" fill="none" stroke="#e3121b" stroke-width="2"/><path d="M4 8l3 3 8-10" fill="none" stroke="#e3121b" stroke-width="2.2"/></svg>Roof Replacement</li>
    <li><svg viewBox="0 0 16 16"><rect x="1" y="3" width="12" height="12" fill="none" stroke="#e3121b" stroke-width="2"/><path d="M4 8l3 3 8-10" fill="none" stroke="#e3121b" stroke-width="2.2"/></svg>Roof Repairs</li>
    <li><svg viewBox="0 0 16 16"><rect x="1" y="3" width="12" height="12" fill="none" stroke="#e3121b" stroke-width="2"/><path d="M4 8l3 3 8-10" fill="none" stroke="#e3121b" stroke-width="2.2"/></svg>Gutters</li>
    <li><svg viewBox="0 0 16 16"><rect x="1" y="3" width="12" height="12" fill="none" stroke="#e3121b" stroke-width="2"/><path d="M4 8l3 3 8-10" fill="none" stroke="#e3121b" stroke-width="2.2"/></svg>Siding</li>
  </ul>
  <ul class="services services-row-two">
    <li><svg viewBox="0 0 16 16"><rect x="1" y="3" width="12" height="12" fill="none" stroke="#e3121b" stroke-width="2"/><path d="M4 8l3 3 8-10" fill="none" stroke="#e3121b" stroke-width="2.2"/></svg>New Construction</li>
    <li><svg viewBox="0 0 16 16"><rect x="1" y="3" width="12" height="12" fill="none" stroke="#e3121b" stroke-width="2"/><path d="M4 8l3 3 8-10" fill="none" stroke="#e3121b" stroke-width="2.2"/></svg>Snow Removal</li>
  </ul>

  <div class="contact">
    <div class="contact-phone">262-555-0147</div>
    <div class="contact-web">harlowridgeconstruction.example</div>
  </div>
  <div class="divider divider-left"></div>

  <div class="brand">
    <span class="brand-square"></span>
    <span class="brand-name">Harlow Ridge<br>Construction</span>
  </div>
  <div class="divider divider-right"></div>

  <div class="badge badge-one" role="img" aria-label="Roofing contractor certification badge"></div>
  <div class="badge badge-two" role="img" aria-label="Shingle manufacturer partner badge"></div>
  <div class="badge badge-three" role="img" aria-label="Accredited business badge"></div>
</main>
</body>
</html>
```